Pelton|Marsh & Quillan business card contest

We need a logo for an upscale boutique diversified company involved in real estate, investments, cattle, and more. Our businesses DO NOT need to be reflected in the business card nor do we want them noted. This is our logo and colors and we love our logo and colors. Our logo looks best against a black background and we like to include the firm name in our logo usage. importantly, the names Pelton and Marsh are separated by | not / and we use an ampersand not the word and.
On the front of the card, we want to include:
company logo and name (Pelton|Marsh & Quillan)
on the back, we would definitely include:
address, email, cell #
logo and name (smaller size than front)

The variable will be location of individual name and title (mine for example is ) - whether on the front OR on the back. interested in variations from which to choose
Dr. Neil R. Whitcombe, CFA
Scientifique des Fusées Financières

we would like to use contemporary symbols for address, email address, cell # with an option for web site that we do not intend to use initially. we like two sided cards and believe this design should use four rounded corners with the standard size. we prefer thicker card stock and may look at metal.

```html
<!DOCTYPE html>
<html lang="en">
<head>
<meta charset="utf-8">
<title>Pelton|Marsh &amp; Quillan — Business Card</title>
<link rel="stylesheet" href="https://fonts.googleapis.com/css2?family=Ubuntu:wght@400;500&display=swap">
<style>
  :root {
    --backdrop: #2a2a2a;
    --card: #1b1b1b;
    --card-back: #161616;
    --orange: #f07a1c;
    --grey: #8a8a8a;
    --grey-light: #a5a5a5;
    --grey-dark: #2e2e2e;
  }
  * { margin: 0; padding: 0; box-sizing: border-box; }
  html, body {
    width: 1200px; height: 960px; overflow: hidden;
    background: var(--backdrop);
    font-family: "Ubuntu", sans-serif;
  }
  .stage {
    position: relative; width: 1200px; height: 960px;
    display: flex; justify-content: center; align-items: center; gap: 70px;
  }
  .card {
    width: 380px; height: 664px;
    border-radius: 18px;
    background: var(--card);
    box-shadow: 0 18px 40px rgba(0,0,0,.45);
    position: relative;
    text-align: center;
  }
  .card--back { background: var(--card-back); }

  .firm-mark {
    display: flex; flex-direction: column; align-items: center; gap: 18px;
    padding-top: 78px;
  }
  .firm-mark__square {
    width: 54px; height: 54px; background: var(--orange);
  }
  .firm-mark__name {
    color: var(--grey); font-size: 25px; font-weight: 400; letter-spacing: .3px;
  }

  .person { margin-top: 58px; }
  .person__name { color: var(--orange); font-size: 25px; font-weight: 500; }
  .person__title { color: var(--grey); font-size: 15.5px; margin-top: 6px; }

  .address { margin-top: 44px; color: var(--grey-light); font-size: 18px; line-height: 1.45; }
  .address__label { color: var(--orange); }

  .contact-icons {
    display: flex; justify-content: center; gap: 16px; margin-top: 30px;
  }
  .contact-icons svg { width: 34px; height: 34px; }

  .contacts { margin-top: 20px; color: var(--grey-light); font-size: 18px; line-height: 1.5; }
  .contacts__phone { font-size: 24px; font-weight: 500; }
  .contacts__accent { color: var(--orange); }

  .back-mark {
    position: absolute; inset: 0;
    display: flex; flex-direction: column; justify-content: center; align-items: center; gap: 26px;
  }
  .back-mark__square {
    width: 140px; height: 140px;
    background: linear-gradient(160deg, #0c0c0c, #2b2b2b);
  }
  .back-mark__name { color: var(--grey-dark); font-size: 24px; font-weight: 400; }
</style>
</head>
<body>
<main class="stage">
  <section class="card card--front" aria-label="Card front">
    <div class="firm-mark">
      <span class="firm-mark__square" aria-hidden="true"></span>
      <span class="firm-mark__name">Pelton|Marsh &amp; Quillan</span>
    </div>

    <div class="person">
      <p class="person__name">Dr. Neil R. Whitcombe, CFA</p>
      <p class="person__title">Scientifique des Fusées Financières</p>
    </div>

    <div class="address">
      <p class="address__label">Address:</p>
      <p>412 Alder Ridge Rd Ste 210</p>
      <p>Larkfield, CA 95403</p>
    </div>

    <div class="contact-icons" aria-hidden="true">
      <svg viewBox="0 0 34 34"><circle cx="17" cy="17" r="17" fill="var(--orange)"/><path d="M12 9.5l3 3-1.6 2.2a11 11 0 0 0 5.9 5.9l2.2-1.6 3 3-1.6 2.4c-6.5.5-13.2-6.2-12.7-12.7z" fill="none" stroke="#1b1b1b" stroke-width="1.8" stroke-linejoin="round"/></svg>
      <svg viewBox="0 0 34 34"><circle cx="17" cy="17" r="17" fill="var(--orange)"/><rect x="9" y="11.5" width="16" height="11" fill="#1b1b1b"/><path d="M9 11.5l8 6.5 8-6.5" fill="none" stroke="var(--orange)" stroke-width="1.4"/></svg>
      <svg viewBox="0 0 34 34"><circle cx="17" cy="17" r="17" fill="var(--orange)"/><g fill="none" stroke="#1b1b1b" stroke-width="1.6"><circle cx="17" cy="17" r="8"/><ellipse cx="17" cy="17" rx="3.5" ry="8"/><path d="M9 17h16M10.5 13h13M10.5 21h13"/></g></svg>
    </div>

    <div class="contacts">
      <p class="contacts__phone">707.555.0148</p>
      <p>Info@pmqoffice.com</p>
      <p>www.<span class="contacts__accent">pmqholdings</span>.com</p>
    </div>
  </section>

  <section class="card card--back" aria-label="Card back">
    <div class="back-mark">
      <span class="back-mark__square" aria-hidden="true"></span>
      <span class="back-mark__name">Pelton|Marsh &amp; Quillan</span>
    </div>
  </section>
</main>
</body>
</html>
```